Informational Website for MOSVALEK-MOSaic VALley Eastern Kinship of Clinic Record Scholars

I need an informational website to help establish us as a legitimate entity. This will help us as we seek funding in to perform the research we intend to carry out. We are a newly formed group of family physicians and primary care researchers from 9 different countries around the world. We have access to electronic medical record data and/or health insurance claims data in our respective countries. We intend to perform international comparative studies in primary care. Our set of projects are to study the impact of the COVID-19 pandemic on primary care in our respective countries and around the world.
I've already purchased a domain and website from Wix. It is a premium account. The domain is https://www.mosvalekclinicnet.org

Target Market(s)

Researchers, policy makers, universities, research funding agencies

Coding

Coded - Design and coding required

Number of Pages Required

5+ page

Font styles to use
Sans Serif

Requirements
Must have
• Must have our logo and an interactive map of the world highlighting Canada, Australia, China (including Hong Kong), Norway, Singapore, South Korea, Sweden, United Kingdom, United States.
This map must be editable such that we can add or remove countries and cities as we evolve. Please see attached brief.
Nice to have
• Nice to depict primary care and big data research

```html
<!DOCTYPE html>
<html lang="en">
<head>
<meta charset="utf-8">
<title>MOSVALEK – MOSaic VALley Eastern Kinship of Clinic Record Scholars</title>
<link rel="stylesheet" href="https://fonts.googleapis.com/css2?family=Montserrat:wght@400;500;600;700&family=Arimo:wght@400;700&display=swap">
<style>
:root{
  --navy:#0b1f6b;
  --navy-deep:#0a1c63;
  --green:#6b9c0b;
  --purple-a:#3d0c86;
  --purple-b:#14053a;
  --ink:#333;
  --muted:#666;
  --soft:#f4f4f4;
  --white:#fff;
  --line:#d9d9d9;
  --star:#f0a020;
}
*{box-sizing:border-box;margin:0;padding:0}
html,body{width:1200px;height:3469px;overflow:hidden}
body{position:relative;background:var(--white);font-family:"Arimo",Arial,sans-serif;color:var(--ink)}
.abs{position:absolute}
.head{font-family:"Montserrat",Arial,sans-serif}

/* header */
.site-header{left:0;top:0;width:1200px;height:123px;background:var(--white);z-index:3}
.brand-badge{left:110px;top:0;width:198px;height:198px;border-radius:50%;background:var(--white);margin-top:-0px;top:0;clip-path:none;z-index:4;display:flex;align-items:center;justify-content:center}
.brand-badge{top:-2px}
.brand-name{font-family:"Montserrat",sans-serif;font-weight:700;font-size:30px;color:var(--navy);letter-spacing:.5px;margin-top:-10px}
.main-nav{left:502px;top:52px;display:flex;gap:0;font-family:"Montserrat",sans-serif;font-weight:600;font-size:14px;color:#222}
.main-nav a{position:absolute;white-space:nowrap;text-decoration:none;color:#222}
.main-nav a.active{color:var(--green)}
.search-btn{left:1037px;top:35px;width:52px;height:52px;border:2px solid var(--green);border-radius:50%;display:flex;align-items:center;justify-content:center}

/* hero */
.hero{left:0;top:123px;width:1200px;height:760px;z-index:1}
.hero-title{left:78px;top:375px;font-family:"Montserrat",sans-serif;font-weight:500;font-size:31px;line-height:50px;color:var(--white);z-index:2}
.hero-title em{font-style:normal;color:var(--green)}
.hero-art{left:525px;top:189px;width:675px;height:606px;border-radius:40px;background:radial-gradient(circle at 55% 55%,#1fa6d8 0%,#1c4fa6 30%,rgba(40,20,110,.4) 60%,rgba(40,20,110,0) 75%);z-index:2}
.btn{display:flex;align-items:center;justify-content:center;border-radius:30px;font-family:"Montserrat",sans-serif;font-weight:600;color:var(--white);text-transform:uppercase}
.hero-btn{left:77px;top:546px;width:175px;height:57px;background:var(--green);font-size:16px;z-index:2}

/* about */
.about-title{left:112px;top:970px;font-size:35px;font-weight:600;color:var(--navy)}
.about-sub{left:112px;top:1020px;width:520px;font-size:25px;line-height:37px;font-weight:500;color:var(--green)}
.about-text{left:112px;top:1112px;width:483px;font-size:13.4px;line-height:25.8px;color:#444;text-align:justify}
.about-btn{left:112px;top:1286px;width:149px;height:54px;background:var(--navy);font-size:14.5px}
.about-mark{left:672px;top:985px;width:480px;height:320px;display:flex;align-items:center;justify-content:center;gap:22px}
.about-mark .dot{width:70px;height:70px;border-radius:50%;background:var(--green)}
.about-mark .name{font-family:"Montserrat",sans-serif;font-weight:700;font-size:62px;color:var(--navy)}

/* services */
.services{left:0;top:1408px;width:1200px;height:545px;background:var(--soft)}
.section-title{width:1200px;text-align:center;font-family:"Montserrat",sans-serif;font-weight:600;font-size:35px;color:var(--navy)}
.section-title span{color:var(--green)}
.section-rule{left:580px;width:40px;height:2px;background:var(--green)}
.service-card{top:1549px;width:237px;height:326px;color:var(--white);text-align:center}
.service-card.navy{background:var(--navy)}
.service-card.green{background:var(--green)}
.service-card svg{position:absolute;left:84px;top:26px}
.service-card h3{position:absolute;top:122px;width:100%;font-family:"Montserrat",sans-serif;font-weight:500;font-size:17px}
.service-card p{position:absolute;top:163px;left:18px;width:201px;font-size:13.4px;line-height:25.6px}
.service-card .ghost{position:absolute;left:59px;top:256px;width:119px;height:40px;border:2px solid var(--white);border-radius:22px;font-size:13.5px}

/* testimonials */
.quote-card{top:2108px;width:312px;height:216px;border:1px solid var(--line);border-bottom:3px solid var(--line);background:var(--white);text-align:center}
.quote-card.featured{border-bottom-color:var(--green)}
.quote-card .mark{position:absolute;top:18px;left:0;width:100%;font-family:Georgia,serif;font-weight:700;font-size:62px;line-height:62px;color:#9a9a9a}
.quote-card.featured .mark{color:var(--green)}
.quote-card p{position:absolute;top:66px;left:13px;width:286px;font-size:13.4px;line-height:24.2px;color:#777}
.quote-card .stars{position:absolute;top:170px;width:100%;font-size:12px;letter-spacing:2px;color:var(--star)}
.quote-tip{top:2320px;width:0;height:0;border-left:11px solid transparent;border-right:11px solid transparent;border-top:11px solid var(--line)}
.quote-tip.featured{border-top-color:var(--green)}
.avatar{top:2349px;width:66px;height:66px;border-radius:50%;background:linear-gradient(135deg,#c9a68a,#6b5140)}
.who{top:2363px;font-family:"Montserrat",sans-serif}
.who b{display:block;font-weight:500;font-size:15px;color:#333}
.who.featured b{color:var(--green)}
.who small{display:block;font-family:"Arimo",sans-serif;font-size:11px;color:#666;margin-top:4px}

/* blog */
.blog-photo{left:112px;top:2532px;width:537px;height:407px;background:linear-gradient(135deg,#1c3a6a 0%,#5d86b5 45%,#d4e2ef 65%,#27476f 100%)}
.blog-panel{left:570px;top:2620px;width:520px;height:354px;background:var(--green);color:var(--white)}
.blog-panel h2{position:absolute;left:42px;top:42px;font-family:"Montserrat",sans-serif;font-weight:500;font-size:36px}
.blog-date{position:absolute;left:44px;top:105px;width:119px;height:30px;background:var(--navy);font-size:10px;display:flex;align-items:center;justify-content:center}
.blog-panel p{position:absolute;left:44px;top:155px;width:442px;font-size:13.4px;line-height:25.8px;text-align:justify}

/* footer */
.site-footer{left:0;top:3041px;width:1200px;height:428px;background:var(--navy-deep);color:var(--white)}
.footer-brand{left:125px;top:3125px;width:262px;height:202px;display:flex;align-items:center;justify-content:center;font-family:"Montserrat",sans-serif;font-weight:700;font-size:46px;color:var(--white)}
.footer-h{top:3100px;font-family:"Montserrat",sans-serif;font-weight:500;font-size:25px}
.quick-links{left:440px;top:3152px;list-style:none;font-family:"Montserrat",sans-serif;font-weight:500;font-size:13px}
.quick-links li{height:34.5px;display:flex;align-items:center;gap:18px}
.quick-links li::before{content:"»";font-size:16px;margin-left:4px}
.contact-list{left:636px;top:3152px;font-size:13.4px;line-height:21px}
.contact-list .row{position:relative;padding-left:28px;margin-bottom:7px}
.contact-list svg{position:absolute;left:0;top:4px}
.news-text{left:859px;top:3152px;width:230px;font-size:13.4px;line-height:28px}
.news-input{left:859px;top:3225px;width:227px;height:44px;background:var(--white);color:#333;font-size:11px;padding-left:18px;display:flex;align-items:center}
.news-btn{left:859px;top:3283px;width:103px;height:40px;background:var(--green);font-size:13px}
.copyright{left:0;top:3418px;width:1200px;text-align:center;font-family:"Montserrat",sans-serif;font-size:15px}
</style>
</head>
<body>

<header class="abs site-header">
  <nav class="abs main-nav">
    <a class="active" style="left:0">HOME</a>
    <a style="left:95px">ABOUT US</a>
    <a style="left:218px">SERVICES</a>
    <a style="left:338px">NEWS</a>
    <a style="left:434px">CONTACT US</a>
  </nav>
  <div class="abs search-btn">
    <svg width="14" height="14" viewBox="0 0 14 14"><circle cx="6" cy="6" r="4" fill="none" stroke="#6b9c0b" stroke-width="2"/><line x1="9" y1="9" x2="12.5" y2="12.5" stroke="#6b9c0b" stroke-width="2"/></svg>
  </div>
</header>
<div class="abs brand-badge"><span class="brand-name">MOSVALEK</span></div>

<section class="abs hero">
  <svg width="1200" height="760" viewBox="0 0 1200 760" style="position:absolute;left:0;top:0">
    <defs>
      <linearGradient id="heroBg" x1="0" y1="0" x2="1" y2="1">
        <stop offset="0" stop-color="#3d0c86"/>
        <stop offset="0.6" stop-color="#1a0648"/>
        <stop offset="1" stop-color="#0e0430"/>
      </linearGradient>
    </defs>
    <path d="M0 0H1200V789L0 788Z" fill="#6b9c0b" transform="translate(0,0)" opacity="0"/>
    <path d="M0 700 L415 755 L1200 788 L1200 700 Z" fill="none"/>
    <path d="M0 0 H1200 V700 L415 755 L0 705 Z" fill="#6b9c0b"/>
    <path d="M0 0 H1200 V665 L415 745 L0 665 Z" fill="url(#heroBg)"/>
    <path d="M0 705 L415 755 L1200 700 L1200 760 L0 760 Z" fill="#fff"/>
    <path d="M0 705 L0 745 L415 755 Z" fill="#6b9c0b"/>
  </svg>
</section>
<h1 class="abs hero-title">MOSaic VALley Eastern<br>Kinship of <em>Clinic Record</em><br>Scholars.</h1>
<div class="abs hero-art" role="img" aria-label="Isometric illustration of researchers at laptops around a glowing data server with floating charts"></div>
<a class="abs btn hero-btn">Read More</a>

<section>
  <h2 class="abs head about-title">ABOUT</h2>
  <p class="abs head about-sub">MOSaic VALley Eastern Kinship of Clinic Record Scholars</p>
  <p class="abs about-text">We are family physicians and primary care researchers from 9 different countries around the world. We have access to electronic medical record data and/or health insurance claims data in our respective countries. We intend to perform international comparative studies in primary care. Our first project is to study the impact of the COVID-19 pandemic on primary care in our respective countries and around the world.</p>
  <a class="abs btn about-btn">Read More</a>
  <div class="abs about-mark"><span class="dot"></span><span class="name">MOSVALEK</span></div>
</section>

<section class="abs services"></section>
<h2 class="abs section-title" style="left:0;top:1455px">OUR <span>SERVICES</span></h2>
<div class="abs section-rule" style="top:1511px"></div>

<div class="abs service-card navy" style="left:112px">
  <svg width="68" height="62" viewBox="0 0 68 62" fill="none" stroke="#fff" stroke-width="2"><rect x="2" y="6" width="64" height="40" rx="2"/><line x1="34" y1="46" x2="34" y2="56"/><line x1="22" y1="56" x2="46" y2="56"/><circle cx="24" cy="24" r="11"/><path d="M24 13v11h11"/><line x1="46" y1="36" x2="46" y2="28"/><line x1="52" y1="36" x2="52" y2="22"/><line x1="58" y1="36" x2="58" y2="16"/></svg>
  <h3>SERVICES 01</h3>
  <p>Sed ut perspiciatis unde om nis iste natus error sit voluptate accusantium doloremque</p>
  <a class="btn ghost">Read More</a>
</div>
<div class="abs service-card green" style="left:359px">
  <svg width="68" height="70" viewBox="0 0 68 70" fill="none" stroke="#fff" stroke-width="2"><rect x="6" y="2" width="56" height="14" rx="5"/><rect x="6" y="20" width="56" height="14" rx="5"/><rect x="6" y="38" width="56" height="14" rx="5"/><circle cx="14" cy="9" r="2"/><circle cx="14" cy="27" r="2"/><circle cx="14" cy="45" r="2"/><line x1="40" y1="6" x2="40" y2="12"/><line x1="46" y1="6" x2="46" y2="12"/><line x1="52" y1="6" x2="52" y2="12"/><line x1="40" y1="24" x2="40" y2="30"/><line x1="46" y1="24" x2="46" y2="30"/><line x1="52" y1="24" x2="52" y2="30"/><line x1="34" y1="52" x2="34" y2="60"/><circle cx="34" cy="63" r="4"/><line x1="2" y1="63" x2="30" y2="63"/><line x1="38" y1="63" x2="66" y2="63"/></svg>
  <h3>SERVICES 02</h3>
  <p>Sed ut perspiciatis unde om nis iste natus error sit voluptate accusantium doloremque</p>
  <a class="btn ghost">Read More</a>
</div>
<div class="abs service-card navy" style="left:606px">
  <svg width="70" height="70" viewBox="0 0 70 70" fill="none" stroke="#fff" stroke-width="2"><rect x="12" y="12" width="46" height="46" rx="3"/><rect x="20" y="20" width="30" height="30"/><text x="35" y="42" fill="#fff" stroke="none" font-family="Arial" font-size="17" text-anchor="middle">AI</text><path d="M22 12V2M30 12V2M40 12V2M48 12V2M22 58v10M30 58v10M40 58v10M48 58v10M12 22H2M12 30H2M12 40H2M12 48H2M58 22h10M58 30h10M58 40h10M58 48h10"/></svg>
  <h3>SERVICES 03</h3>
  <p>Sed ut perspiciatis unde om nis iste natus error sit voluptate accusantium doloremque</p>
  <a class="btn ghost">Read More</a>
</div>
<div class="abs service-card green" style="left:853px">
  <svg width="70" height="70" viewBox="0 0 70 70" fill="none" stroke="#fff" stroke-width="2"><rect x="22" y="2" width="26" height="14" rx="2"/><line x1="35" y1="16" x2="35" y2="24"/><path d="M35 24l10 10-10 10-10-10z"/><line x1="25" y1="34" x2="12" y2="34"/><line x1="12" y1="34" x2="12" y2="46"/><line x1="45" y1="34" x2="58" y2="34"/><line x1="58" y1="34" x2="58" y2="46"/><rect x="4" y="46" width="16" height="18" rx="4"/><circle cx="35" cy="56" r="8"/><circle cx="58" cy="56" r="8"/><line x1="35" y1="44" x2="35" y2="48"/></svg>
  <h3>SERVICES 04</h3>
  <p>Sed ut perspiciatis unde om nis iste natus error sit voluptate accusantium doloremque</p>
  <a class="btn ghost">Read More</a>
</div>

<h2 class="abs section-title" style="left:0;top:2021px">OUR <span>TESTIMONIALS</span></h2>
<div class="abs section-rule" style="top:2078px"></div>

<div class="abs quote-card" style="left:112px"><div class="mark">“</div><p>Sed ut perspiciatis unde omnis iste natus error sit voluptatem accusantium doloremque lauda ntium, totam rem aperiam, eaque ipsa quae vitae dicta sunt explicabo.</p><div class="stars">☆☆☆☆☆</div></div>
<div class="abs quote-card featured" style="left:445px"><div class="mark">“</div><p>Sed ut perspiciatis unde omnis iste natus error sit voluptatem accusantium doloremque lauda ntium, totam rem aperiam, eaque ipsa quae vitae dicta sunt explicabo.</p><div class="stars">☆☆☆☆☆</div></div>
<div class="abs quote-card" style="left:778px"><div class="mark">“</div><p>Sed ut perspiciatis unde omnis iste natus error sit voluptatem accusantium doloremque lauda ntium, totam rem aperiam, eaque ipsa quae vitae dicta sunt explicabo.</p><div class="stars">☆☆☆☆☆</div></div>
<div class="abs quote-tip" style="left:254px"></div>
<div class="abs quote-tip featured" style="left:589px"></div>
<div class="abs quote-tip" style="left:921px"></div>

<div class="abs avatar" role="img" aria-label="Portrait photo of reviewer" style="left:160px"></div>
<div class="abs who" style="left:238px"><b>Jhon Smith</b><small>Sed ut perspiciatis</small></div>
<div class="abs avatar" role="img" aria-label="Portrait photo of reviewer" style="left:493px"></div>
<div class="abs who featured" style="left:571px"><b>Jhon Smith</b><small>Sed ut perspiciatis</small></div>
<div class="abs avatar" role="img" aria-label="Portrait photo of reviewer" style="left:825px"></div>
<div class="abs who" style="left:903px"><b>Jhon Smith</b><small>Sed ut perspiciatis</small></div>

<div class="abs blog-photo" role="img" aria-label="Photo of a hand touching a tablet with glowing binary data overlay"></div>
<article class="abs blog-panel">
  <h2>LATEST BLOG</h2>
  <div class="blog-date">31 DECEMBER 2020</div>
  <p>Sed ut perspiciatis unde omnis iste natus error sit voluptatem accusant ium doloremque laudantium, totam rem aperiam, eaque ipsa quae ab illo inventore veritatis et quasi architecto beatae vitae dicta sunt explicabo. Nemo enim ipsam voluptatem quia voluptas sit aspernatur aut odit aut fugit, sed quia consequuntur magni dolores eos qui ratione voluptatem iste natus error sit sequi nesciunt.</p>
</article>

<footer class="abs site-footer"></footer>
<div class="abs footer-brand">MOSVALEK</div>
<h3 class="abs footer-h" style="left:440px;color:#fff">Quick Links</h3>
<ul class="abs quick-links" style="color:#fff">
  <li>HOME</li><li>ABOUT US</li><li>SERVICES</li><li>NEWS</li><li>CONTACT US</li>
</ul>
<h3 class="abs footer-h" style="left:636px;top:3102px;color:#fff">Contact</h3>
<div class="abs contact-list" style="color:#fff">
  <div class="row"><svg width="12" height="16" viewBox="0 0 12 16"><path d="M6 0a6 6 0 0 0-6 6c0 4.5 6 10 6 10s6-5.5 6-10a6 6 0 0 0-6-6z" fill="#fff"/><circle cx="6" cy="6" r="2.2" fill="#0a1c63"/></svg>Address :<br>#15 Lorem Ipsum Dummy<br>Lorem Ipsum Dummy</div>
  <div class="row"><svg width="14" height="14" viewBox="0 0 14 14"><path d="M3 1l2.5 3-1.5 1.5c.8 1.8 2.2 3.2 4 4L9.5 8l3 2.5-1.5 2.5C6 13 1 8 1 2.5z" fill="#fff"/></svg>Phone :<br>(000) 123-1231</div>
  <div class="row"><svg width="14" height="11" viewBox="0 0 14 11"><rect width="14" height="11" rx="1" fill="#fff"/><path d="M1 1l6 5 6-5" fill="none" stroke="#0a1c63" stroke-width="1.4"/></svg>Email :<br>info@companyname.com</div>
</div>
<h3 class="abs footer-h" style="left:859px;color:#fff">Newsletter</h3>
<p class="abs news-text" style="color:#fff">Sed ut perspiciatis unde omnis nat us error sit voluptatem</p>
<div class="abs news-input">Enter Email Id :</div>
<a class="abs btn news-btn">Submit</a>
<p class="abs copyright" style="color:#fff">© Copyright 2020 Mosvalek Primary Care.All Rights Reserved</p>

</body>
</html>
```